Stationery Design Project for Bramble Co

Hi All,

We need you to design stationary for a new online financial services business. We have already got the logo designed and it is attached. If you would like it in any other formats please let me know. If you could also if possible, match the fonts in your design to that on the logo’s provided.

What we need:
- Business Card
- A4 Letter head
- A4 Folders
- PPT template (Title page and regular page)

And what ever else you want to throw in.

We are in the process of getting the web site designed, however below is a list of websites which we like which will give you an understanding of the style that we are going for.

- plimo.com
- brambleroute.com
- tallowquay.com
- pelkwintry.com

I look forward to your seeing your design.

Industry/Entity Type

Financial

Requirements
Must have
• Outputs:
- Documents ready to print
- Generic editable information
- Pdf copies of the documents
- Word version of letterhead

```html
<!DOCTYPE html>
<html lang="en">
<head>
<meta charset="utf-8">
<title>Bramble Co Stationery</title>
<link rel="stylesheet" href="https://fonts.googleapis.com/css2?family=Didact+Gothic&display=swap">
<style>
  :root {
    --backdrop: #ebe8e4;
    --paper: #ffffff;
    --brand-blue: #0b7fa9;
    --brand-orange: #f39a1c;
    --ink-navy: #1d3550;
    --soft-peach: #fde3c6;
    --text-grey: #4a5563;
  }
  * { margin: 0; padding: 0; box-sizing: border-box; }
  html, body { width: 1200px; height: 900px; overflow: hidden; }
  body {
    position: relative;
    background: var(--backdrop);
    font-family: "Didact Gothic", "Century Gothic", sans-serif;
    color: var(--text-grey);
  }
  .sheet { position: absolute; background: var(--paper); overflow: hidden; }

  .wordmark { position: absolute; display: flex; align-items: center; gap: 8px; color: var(--ink-navy); white-space: nowrap; }
  .wordmark-dot { border-radius: 50%; background: var(--brand-orange); flex: none; }

  .contact { position: absolute; line-height: 1.3; white-space: nowrap; }

  .deco-circle { position: absolute; border-radius: 50%; }

  /* Letterhead */
  .letterhead { left: 80px; top: 58px; width: 548px; height: 777px; }
  .letterhead .wordmark { left: 25px; top: 30px; font-size: 21px; }
  .letterhead .wordmark-dot { width: 26px; height: 26px; }
  .letterhead .contact { left: 417px; top: 26px; font-size: 7px; }
  .letterhead .deco-circle { left: -170px; top: 447px; width: 340px; height: 340px; background: var(--soft-peach); }

  /* Envelope */
  .envelope-flap { position: absolute; left: 549px; top: 75px; }
  .envelope { left: 549px; top: 196px; width: 581px; height: 269px; }
  .envelope .wordmark { left: 392px; top: 30px; font-size: 19px; }
  .envelope .wordmark-dot { width: 24px; height: 24px; }
  .envelope .contact { left: 429px; top: 58px; font-size: 6.5px; }
  .envelope .deco-circle { left: -130px; top: 10px; width: 260px; height: 260px; background: var(--soft-peach); }

  /* Business card back */
  .card-back { left: 880px; top: 549px; width: 250px; height: 141px; background: var(--brand-blue); }
  .card-back .wordmark { left: 68px; top: 60px; font-size: 15px; color: var(--paper); gap: 6px; }
  .card-back .wordmark-dot { width: 18px; height: 18px; }

  /* Business card front */
  .card-front { left: 701px; top: 663px; width: 250px; height: 170px; }
  .card-front .deco-circle { left: -98px; top: -13px; width: 196px; height: 196px; background: var(--brand-orange); }
  .card-front .holder { position: absolute; left: 123px; top: 32px; white-space: nowrap; }
  .card-front .holder-name { font-size: 12px; color: var(--brand-orange); font-weight: 700; }
  .card-front .holder-role { font-size: 7px; }
  .card-front .contact { left: 123px; top: 66px; font-size: 6.5px; }
  .contact p + p.gap { margin-top: 5px; }
</style>
</head>
<body>

  <section class="sheet letterhead" aria-label="Letterhead">
    <div class="wordmark"><span class="wordmark-dot"></span>brambleco.com</div>
    <div class="contact">
      <p>418 Corrin Street, 5th floor</p>
      <p>Halden, NY 10940</p>
      <p class="gap">T: 555-201-4480</p>
      <p>F: 555-201-4491</p>
    </div>
    <div class="deco-circle"></div>
  </section>

  <svg class="envelope-flap" width="581" height="122" viewBox="0 0 581 122" aria-hidden="true">
    <path d="M0 122 L4 102 Q10 96 30 92 L268 6 Q290 -2 312 6 L550 92 Q572 96 577 102 L581 122 Z" fill="var(--brand-blue)"/>
  </svg>
  <section class="sheet envelope" aria-label="Envelope">
    <div class="deco-circle"></div>
    <div class="wordmark"><span class="wordmark-dot"></span>brambleco.com</div>
    <div class="contact">
      <p>418 Corrin Street, 5th floor</p>
      <p>Halden, NY 10940</p>
      <p class="gap">T: 555-201-4480 | F: 555-201-4491</p>
    </div>
  </section>

  <section class="sheet card-back" aria-label="Business card back">
    <div class="wordmark"><span class="wordmark-dot"></span>brambleco.com</div>
  </section>

  <section class="sheet card-front" aria-label="Business card front">
    <div class="deco-circle"></div>
    <div class="holder">
      <p class="holder-name">Milo Harrow</p>
      <p class="holder-role">Co-founder</p>
    </div>
    <div class="contact">
      <p>418 Corrin Street, 5th floor</p>
      <p>Halden, NY 10940</p>
      <p class="gap">T: 555-201-4480 ext 345</p>
      <p>F: 555-201-4491</p>
      <p>E: yourname@brambleco.com</p>
    </div>
  </section>

</body>
</html>
```